Building Referrer Relationships Booklet

4 page A4 booklet to give to potential professional referrers to establish a collaborative relationship.Needs to be bright, vibrant, colourful, friendly, inviting, in keeping with The Stride Studio colours.
Want to provide potential referrer partners a great reason to choose to collaborate with us. They need to know who we are, what makes us different/appealing, and who we are looking for to connect with.
The final product should communicate high performance and connectedness.

Target Market(s)

professional medical allied health and fitness practitioners

Industry/Entity Type

Health

Requirements
Must have
• energetic, vibrant, engaging, inviting, images

```html
<!DOCTYPE html>
<html lang="en">
<head>
<meta charset="utf-8">
<title>The Stride Studio – Referral Partnerships Booklet</title>
<link href="https://fonts.googleapis.com/css2?family=Raleway:wght@400;500;600;700;800&family=Open+Sans:wght@400;600;700&display=swap" rel="stylesheet">
<style>
:root{
  --navy:#2b2f8f;
  --blue:#2f5fb8;
  --royal:#3a4fb0;
  --violet:#4b2f93;
  --orange:#f07a1a;
  --amber:#f5a21b;
  --ink:#2b2b2b;
  --grey:#5d5d5d;
  --paper:#ffffff;
  --backdrop-top:#6f6e6e;
  --backdrop-bottom:#1d1a1a;
}
*{margin:0;padding:0;box-sizing:border-box}
html,body{width:869px;height:1200px;overflow:hidden}
body{background:linear-gradient(180deg,var(--backdrop-top),#3a3636 55%,var(--backdrop-bottom));font-family:"Open Sans",Arial,sans-serif;color:var(--ink)}
.canvas{position:relative;width:869px;height:1200px}
.page{position:absolute;background:var(--paper);overflow:hidden}
.abs{position:absolute}
.photo{position:absolute}
.round{border-radius:50%;border:3px solid var(--orange);box-shadow:0 0 0 2px #fff}
.tab{position:absolute;background:linear-gradient(90deg,var(--orange),#f39a2b);color:#fff;font:700 9.5px "Raleway",sans-serif;padding:2px 0 0 28px;height:15px;border-bottom:2px solid #c55d0d}
.brand-mark{position:absolute;text-align:center}
.brand-mark .disc{width:100%;aspect-ratio:1;border-radius:50%;background:radial-gradient(circle at 40% 35%,#4e6fd0,var(--navy));border:3px solid var(--orange)}
.brand-mark .name{font:700 10px "Raleway",sans-serif;color:var(--navy);margin-top:3px;white-space:nowrap}
.h-display{font-family:"Raleway",sans-serif;font-weight:800;color:var(--navy)}
.partners-title{font:800 11.5px "Raleway",sans-serif;color:var(--amber);letter-spacing:.2px}
.partner-col{position:absolute;width:100px}
.partner-col h4{font:700 7px "Raleway",sans-serif;color:var(--amber);margin-top:5px;position:relative;padding-left:6px}
.partner-col h4::before{content:"";position:absolute;left:0;top:2.5px;width:3px;height:3px;background:var(--amber);border-radius:50%}
.partner-col p{font-size:5.7px;line-height:1.4;color:#fff;padding-left:6px}
.contact{position:absolute;font-size:6px;line-height:1.45;color:var(--grey)}
.contact b{color:var(--navy);font-family:"Raleway",sans-serif;font-size:7px}
.contact .row{display:flex;align-items:center;gap:3px}
.contact .web{color:var(--navy);font-weight:700;font-size:7px}
.badge{position:absolute;border-radius:4px}
.values-list{position:absolute;list-style:none;width:56px}
.values-list li{font:600 7px "Raleway",sans-serif;color:#fff;padding:3px 0 3px 10px;border-bottom:1px solid rgba(255,255,255,.35);position:relative;letter-spacing:.3px}
.values-list li::before{content:"";position:absolute;left:0;top:5px;width:5px;height:2.5px;border-left:1.5px solid var(--amber);border-bottom:1.5px solid var(--amber);transform:rotate(-45deg)}
.value-text{position:absolute;width:122px;font-size:5.6px;line-height:1.35;color:#fff}
.value-text p{margin-bottom:5px}
.value-text b{color:var(--amber)}
.lead{position:absolute;font:400 15.5px/1.25 "Raleway",sans-serif;color:var(--blue);text-align:center}
.lead b{color:var(--orange);font-weight:700}
.love-item{position:absolute;display:flex;gap:7px;align-items:flex-start}
.love-item .num{width:19px;height:19px;border:1.3px solid var(--orange);border-radius:50%;font:600 8px/17px "Raleway",sans-serif;color:var(--orange);text-align:center;flex:none}
.love-item h5{font:700 7.6px "Open Sans",sans-serif;color:var(--ink)}
.love-item p{font-size:5.6px;color:var(--grey)}
.team-member{position:absolute;top:0;width:46px;text-align:center}
.team-member .shot{height:66px;border-radius:2px}
.team-member .nm{font:700 5.6px "Open Sans",sans-serif;color:var(--ink);margin-top:3px;white-space:nowrap}
.team-member .rl{font-size:4.6px;color:var(--grey)}
.way-list{position:absolute;list-style:none;font-size:5.8px;line-height:1.3;color:var(--ink)}
.way-list .step{font:700 6.4px "Raleway",sans-serif;color:var(--navy);margin-top:6px}
.way-list .step span{color:var(--orange)}
.way-list .step small{font:400 5.6px "Open Sans",sans-serif;color:var(--ink);display:block}
.way-list li.pt{padding-left:6px;position:relative;margin-top:1.5px}
.way-list li.pt::before{content:"";position:absolute;left:0;top:2.5px;width:2.5px;height:2.5px;background:var(--orange)}
.elite h4{font:700 8px "Raleway",sans-serif;color:var(--amber);margin-bottom:2px}
.elite li{list-style:none;font-size:5.9px;line-height:1.35;color:#fff;padding-left:8px;position:relative}
.elite li::before{content:"";position:absolute;left:0;top:1.5px;width:4px;height:2px;border-left:1.3px solid var(--amber);border-bottom:1.3px solid var(--amber);transform:rotate(-45deg)}
.caption{position:absolute;font-size:4.4px;color:var(--grey)}
.url{position:absolute;font:700 6.6px "Open Sans",sans-serif}
.cover-headline{position:absolute;right:26px;top:410px;text-align:right;font:800 18.5px/1.2 "Raleway",sans-serif;color:#fff;text-shadow:0 1px 2px rgba(20,20,60,.35)}
</style>
</head>
<body>
<main class="canvas">

  <!-- ===== Spread 1 : back cover (left) ===== -->
  <section class="page page-about-you" style="left:56px;top:52px;width:378px;height:535px">
    <div class="photo" role="img" aria-label="Therapist massaging a client's shoulder and back" style="left:0;top:0;width:378px;height:205px;background:linear-gradient(120deg,#e9e4df,#c9b3a3 45%,#7d6a60 75%,#3e3836)"></div>
    <svg class="abs" style="left:0;top:0" width="378" height="535" viewBox="0 0 378 535" aria-hidden="true">
      <defs>
        <linearGradient id="bandA" x1="0" y1="0" x2="1" y2="1">
          <stop offset="0" stop-color="#4a2e92"/><stop offset=".55" stop-color="#2d4fb0"/><stop offset="1" stop-color="#2f6bc4"/>
        </linearGradient>
      </defs>
      <path d="M0 215 C120 170 250 160 378 130 L378 430 C280 400 150 400 0 420 Z" fill="url(#bandA)"/>
      <path d="M0 215 C120 170 250 160 378 130 L378 140 C250 170 120 182 0 225 Z" fill="#fff"/>
      <path d="M110 405 C200 398 300 410 378 430 L378 445 C300 425 200 414 110 418 Z" fill="var(--orange)"/>
      <path d="M0 420 C150 400 280 400 378 430 L378 535 L0 535 Z" fill="#fff"/>
    </svg>
    <div class="tab" style="left:0;top:18px;width:96px">About You</div>
    <div class="photo round" role="img" aria-label="Woman relaxing during a back massage" style="left:238px;top:115px;width:88px;height:88px;background:radial-gradient(circle at 40% 40%,#f1d8c6,#c79a80 70%,#8e6a57)"></div>

    <div class="partners-title abs" style="left:24px;top:210px">REFERRAL PARTNERS REQUIRED:</div>
    <div class="partner-col" style="left:22px;top:244px">
      <h4>Massage Therapists</h4><p>Deep tissue and remedial massage<br>Therapeutic massage</p>
      <h4>Fascial Therapists</h4><p>Fascial pathway releases to reset the alignment of the whole body</p>
      <h4>Physiotherapists</h4><p>Pain relief, protect and strengthen both lower limb and upper limb</p>
    </div>
    <div class="partner-col" style="left:130px;top:244px">
      <h4>GPs, Sports Physicians</h4><p>General health, diagnostics, treatment support, prescription medications<br>Specialist referrals</p>
      <h4>Osteopaths, Chiropractors</h4><p>Mobilisation and manipulative therapy for the spinal column and limbs</p>
      <h4>Dieticians, Nutritionists</h4><p>DEXA scan for bone density/ lean mass/fat mass<br>Optimising gut health and nutrition - You are what you eat!</p>
    </div>
    <div class="partner-col" style="left:236px;top:244px;width:120px">
      <h4>Psychologists, Psychiatrists</h4><p>Sometimes our physical body cannot get better until we optimise a healthy mind</p>
      <h4>Personal Trainers, Pilates and Yoga Instructors</h4><p>Create awesome body strength, flexibility and resilience</p>
      <h4>Surgeons</h4><p>When conservative methods are ineffective, surgical intervention works well.</p>
      <h4>Other Partners</h4><p>For other biohacks we haven't even thought of yet!</p>
    </div>
    <div class="photo" role="img" aria-label="Hands supporting a client's foot" style="left:44px;top:372px;width:72px;height:42px;border-radius:4px;background:linear-gradient(90deg,#d8c3b3,#f2e4d8)"></div>

    <div class="brand-mark" style="left:30px;top:437px;width:58px"><div class="disc"></div><div class="name">The Stride Studio</div></div>
    <div class="contact" style="left:124px;top:460px">
      <b>The Stride Studio</b>
      <div class="row"><svg width="6" height="7" viewBox="0 0 6 7"><path d="M3 0a2.5 2.5 0 0 1 2.5 2.5C5.5 4.5 3 7 3 7S.5 4.5.5 2.5A2.5 2.5 0 0 1 3 0z" fill="var(--orange)"/></svg>Harbour Central</div>
      <div style="padding-left:9px">4 / 218 Marine Pde<br>Seabrook WA 6099</div>
      <div class="row" style="margin-top:8px"><svg width="6" height="6" viewBox="0 0 6 6"><circle cx="3" cy="3" r="3" fill="var(--orange)"/></svg><span style="color:var(--navy);font-weight:700">(08) 9000 4172</span></div>
      <div class="row"><svg width="6" height="6" viewBox="0 0 6 6"><circle cx="3" cy="3" r="3" fill="var(--orange)"/></svg><span class="web">www.thestridestudio.net</span></div>
    </div>
    <div class="abs" style="left:240px;top:455px;width:1px;height:70px;background:#ccc"></div>
    <div class="badge" style="left:250px;top:457px;width:44px;height:14px;background:#e7eaf4"></div>
    <div class="badge" style="left:312px;top:456px;width:46px;height:20px;background:#e6ecf7"></div>
    <div class="badge" style="left:250px;top:480px;width:48px;height:14px;background:#f4dcdc"></div>
    <div class="badge" style="left:312px;top:481px;width:42px;height:16px;background:#fbeec9"></div>
    <div class="badge" style="left:250px;top:505px;width:44px;height:16px;background:#f4e1e1"></div>
  </section>

  <!-- ===== Spread 1 : front cover (right) ===== -->
  <section class="page page-cover" style="left:434px;top:52px;width:379px;height:535px">
    <h1 class="h-display abs" style="left:28px;top:30px;font-size:24.5px;line-height:1.13">Referral<br>Partnerships</h1>
    <div class="abs" style="left:29px;top:94px;font:500 11.5px 'Raleway',sans-serif;color:#333">Because Together We Achieve More</div>
    <div class="brand-mark" style="left:281px;top:52px;width:66px"><div class="disc"></div><div class="name" style="font-size:10.5px">The Stride Studio</div></div>
    <div class="photo" role="img" aria-label="Team joining hands together in a circle" style="left:0;top:150px;width:379px;height:300px;background:radial-gradient(circle at 55% 40%,#c79a7a,#8b6a55 40%,#a89a8f 70%,#d8cfc6)"></div>
    <svg class="abs" style="left:0;top:0" width="379" height="535" viewBox="0 0 379 535" aria-hidden="true">
      <defs>
        <linearGradient id="coverBand" x1="0" y1="0" x2="1" y2="0">
          <stop offset="0" stop-color="#2f5fbf"/><stop offset=".6" stop-color="#3a45a8"/><stop offset="1" stop-color="#4a2f93"/>
        </linearGradient>
      </defs>
      <path d="M0 130 L379 130 L379 150 C250 135 120 140 0 160 Z" fill="#fff"/>
      <path d="M0 140 C120 130 260 128 379 150 L379 163 C260 142 120 146 0 155 Z" fill="var(--orange)"/>
      <path d="M0 445 C120 418 250 386 379 352 L379 535 L0 535 Z" fill="url(#coverBand)"/>
      <path d="M0 434 C120 407 250 375 379 341 L379 352 C250 386 120 418 0 445 Z" fill="#fff" opacity=".95"/>
    </svg>
    <div class="cover-headline">We are all here to<br>help our clients <span style="color:var(--amber)">get</span><br><span style="color:var(--amber)">back on their feet.</span></div>
    <div class="url" style="left:27px;top:498px;color:#fff">www.thestridestudio.net</div>
    <div class="abs" style="right:28px;top:490px;font:400 15px 'Raleway',sans-serif;color:#fff">Let's Do It Together!</div>
  </section>

  <!-- ===== Spread 2 : page 2 (left) ===== -->
  <section class="page page-about-us" style="left:56px;top:622px;width:378px;height:536px">
    <svg class="abs" style="left:0;top:0" width="378" height="536" viewBox="0 0 378 536" aria-hidden="true">
      <defs>
        <linearGradient id="bandB" x1="0" y1="0" x2="1" y2="0">
          <stop offset="0" stop-color="#2f5fbf"/><stop offset=".5" stop-color="#3a45a8"/><stop offset="1" stop-color="#4a2f93"/>
        </linearGradient>
      </defs>
      <path d="M0 0 L378 0 L378 122 C260 128 120 150 0 175 Z" fill="url(#bandB)"/>
      <path d="M150 150 C240 136 310 128 378 126 L378 140 C310 142 240 150 150 163 Z" fill="var(--orange)"/>
    </svg>
    <div class="tab" style="left:0;top:31px;width:96px">About Us</div>
    <ul class="values-list" style="left:38px;top:54px">
      <li>COURAGE</li><li>INSPIRATION</li><li>FUN</li><li>CREATIVE</li><li>WOW</li><li>TEAM</li>
    </ul>
    <div class="value-text" style="left:108px;top:34px">
      <p><b>Courage</b> gives us the strength and confidence to take risks and embrace challenges</p>
      <p><b>Inspiration</b> is our energy, our fuel for success, that life force that feeds us as we grow and develop.</p>
      <p><b>Fun</b> generates happiness, and we all function at our best when we are happy.</p>
      <p><b>Creativity</b> sets us as an innovative leading-edge business.</p>
    </div>
    <div class="value-text" style="left:241px;top:34px;width:118px">
      <p><b>Wow</b> defines us as high performers who do whatever it takes to create the most exceptional and enjoyable experiences for everyone</p>
      <p><b>Team</b> means we work together and depend on each other, so we may accomplish much more than each of us alone.</p>
    </div>
    <div class="photo round" role="img" aria-label="Feet standing on a pressure scanning plate" style="left:164px;top:136px;width:64px;height:64px;background:linear-gradient(160deg,#e8e3de,#b3a49a)"></div>
    <div class="photo round" role="img" aria-label="Clinician reviewing foot scans on a monitor" style="left:222px;top:120px;width:70px;height:70px;background:linear-gradient(160deg,#d6dbe3,#6e7889)"></div>

    <p class="lead" style="left:20px;top:224px;width:340px">At <b>The Stride Studio</b>, we are<br>passionate about building strong postural<br>foundations, from the feet up.</p>
    <div class="abs" style="left:132px;top:290px;font:500 10px/1.25 'Raleway',sans-serif;color:#222">The top 3 things our clients love<br>about us (and hopefully yours will too!)</div>
    <div class="photo" role="img" aria-label="Sole of a foot with muscles highlighted" style="left:28px;top:302px;width:68px;height:86px;border-radius:50%;background:radial-gradient(circle at 50% 45%,#8a6b5a,#3b2d27 60%,#111)"></div>
    <div class="love-item" style="left:130px;top:320px"><div class="num">01</div><div><h5>Positive energy, enthusiasm and outcomes</h5><p>NPS average score &gt;9 out of 10</p></div></div>
    <div class="love-item" style="left:130px;top:345px"><div class="num">02</div><div><h5>Trusted leader in the practice of podiatric medicine</h5><p>established 1999, elite experience; latest high-tech equipment</p></div></div>
    <div class="love-item" style="left:130px;top:370px"><div class="num">03</div><div><h5>Focus is on strong feet, not just orthotics!</h5><p>Groundwork Barefoot Method, Fascial Pathways, Foot Manual Therapies</p></div></div>

    <div class="abs" style="left:20px;top:397px;width:338px;height:1px;background:#ccc"></div>
    <div class="abs" style="left:18px;top:402px;width:13px;height:92px;background:var(--blue);color:#fff;font:700 7px 'Raleway',sans-serif;writing-mode:vertical-rl;transform:rotate(180deg);text-align:center;line-height:13px">Our Team</div>
    <div class="abs" style="left:36px;top:420px;width:322px;height:102px">
      <div class="team-member" style="left:0"><div class="shot" role="img" aria-label="Portrait of a podiatrist" style="background:linear-gradient(#c9cfd8,#e7eaee)"></div><div class="nm">Dr Milo Tan</div><div class="rl">(Podiatrist)</div></div>
      <div class="team-member" style="left:54px"><div class="shot" role="img" aria-label="Portrait of a podiatrist" style="background:linear-gradient(#3a2d2a,#222)"></div><div class="nm">Dr Ada Fenwick</div><div class="rl">(Podiatrist)</div></div>
      <div class="team-member" style="left:108px"><div class="shot" role="img" aria-label="Portrait of the senior podiatrist" style="background:linear-gradient(#b84a4a,#c82c2c)"></div><div class="nm">Dr Clara Voss</div><div class="rl">(Senior Podiatrist)</div></div>
      <div class="team-member" style="left:164px"><div class="shot" role="img" aria-label="Portrait of the principal podiatrist" style="background:linear-gradient(#5a4638,#dfe3ea)"></div><div class="nm">Dr Ravi Kandaswamy</div><div class="rl">(Principal Podiatrist)</div></div>
      <div class="team-member" style="left:222px"><div class="shot" role="img" aria-label="Portrait of the practice manager" style="background:linear-gradient(#c2a890,#2a2a2a)"></div><div class="nm">Tess Holloway</div><div class="rl">(Practice Manager)</div></div>
      <div class="team-member" style="left:276px"><div class="shot" role="img" aria-label="Portrait of the front office administrator" style="background:linear-gradient(#6b4a3a,#1f1f1f)"></div><div class="nm">Jill Parry</div><div class="rl">(Front Office Administrator)</div></div>
    </div>
    <div class="url" style="left:20px;top:516px;color:var(--navy)">www.thestridestudio.net</div>
  </section>

  <!-- ===== Spread 2 : page 3 (right) ===== -->
  <section class="page page-way" style="left:434px;top:622px;width:379px;height:536px">
    <h2 class="abs" style="left:31px;top:30px;font:700 12px 'Raleway',sans-serif;color:var(--navy)">The <span style="color:var(--orange)">Stride</span> Studio Way</h2>
    <p class="abs" style="left:31px;top:46px;width:250px;font-size:5.8px;line-height:1.4;color:#333">Our pathway to strengthen postural foundations, to create lasting changes for freedom of movement, and ultimately keep us going well beyond what we thought was possible (updated as research and tech changes)</p>
    <div class="brand-mark" style="left:290px;top:16px;width:48px"><div class="disc"></div><div class="name" style="font-size:8px">The Stride Studio</div></div>

    <div class="photo" role="img" aria-label="Group photo of workshop participants" style="left:31px;top:78px;width:223px;height:96px;background:linear-gradient(180deg,#c94a3a,#b07a62 45%,#6a5a52)"></div>
    <div class="caption" style="left:31px;top:177px">Structural essentials workshop with Nora Quill</div>
    <div class="photo" role="img" aria-label="Workshop participants practising movement in a hall" style="left:272px;top:86px;width:84px;height:132px;background:linear-gradient(180deg,#d8d2c8,#7c6a5c)"></div>
    <div class="photo" role="img" aria-label="Presenter demonstrating an exercise to a group" style="left:272px;top:244px;width:84px;height:84px;background:linear-gradient(180deg,#ece8e2,#6f6a66)"></div>
    <div class="photo" role="img" aria-label="Two presenters speaking at a seminar" style="left:272px;top:341px;width:84px;height:82px;background:linear-gradient(180deg,#e9e5df,#8d7a6d)"></div>

    <div class="tab" style="left:31px;top:190px;width:96px;padding-left:6px">Fix Your Feet</div>
    <div class="tab" style="left:149px;top:190px;width:105px;padding-left:6px">Biohack Your Body</div>
    <ul class="way-list" style="left:31px;top:206px;width:112px">
      <li class="step">1. <span>Fix</span> the pain</li>
      <li class="pt">Provide analgesia</li><li class="pt">Reduce inflammation</li><li class="pt">Corn/callus/foreign body removal</li><li class="pt">Ingrown/thickened toenail repair and maintenance</li><li class="pt">Surgery</li>
      <li class="step">2. <span>Protect</span> the feet<small>(reduce damage, optimise stability, promote healing)</small></li>
      <li class="pt">Reduce tissue damage</li><li class="pt">Optimise Foot Posture</li><li class="pt">Activate neuromuscular/reflexive balance stability</li><li class="pt">Promote tissue repair/cellular regeneration</li>
      <li class="step">3. <span>Strengthen</span> the feet<small>(increase strength and resilience)</small></li>
      <li class="pt">Strengthen intrinsics</li><li class="pt">Connect foot strength to core strength</li><li class="pt">Stimulate neuromuscular strength</li>
    </ul>
    <ul class="way-list" style="left:149px;top:188px;width:112px">
      <li class="step" style="margin-top:20px">4. <span>Protect</span> the whole body (stability)</li>
      <li class="pt">Optimise Postural Alignment</li><li class="pt">Activate neuromuscular/reflexive balance stability</li><li class="pt">Customised corrective exercises</li><li class="pt">Improve cellular regeneration</li><li class="pt">Optimise nutrition/healthy gut</li><li class="pt">Optimise healthy mind</li>
      <li class="step">5. <span>Strengthen</span> the whole body<small>(strength, elasticity)</small></li>
      <li class="pt">Strengthen the deep core (stabilisers)</li><li class="pt">Strengthen the outer core (mobilisers)</li><li class="pt">Increase fascial elasticity/strength</li><li class="pt">Increase functional strength</li><li class="pt">Increase endurance</li><li class="pt">Customised nutrition for specific performance</li><li class="pt">Improve psychological resilience</li>
      <li class="step">6. <span>Repeat</span> consistently</li>
    </ul>

    <svg class="abs" style="left:0;top:0" width="379" height="536" viewBox="0 0 379 536" aria-hidden="true">
      <defs>
        <linearGradient id="eliteBand" x1="0" y1="0" x2="1" y2="0">
          <stop offset="0" stop-color="#2f5fbf"/><stop offset="1" stop-color="#4a2f93"/>
        </linearGradient>
      </defs>
      <path d="M230 442 C290 430 340 416 379 400 L379 536 L230 536 Z" fill="url(#eliteBand)"/>
      <path d="M240 436 C300 422 345 408 379 392 L379 402 C345 418 300 432 240 444 Z" fill="var(--orange)"/>
    </svg>
    <div class="photo" role="img" aria-label="Masters athletes lined up on a running track" style="left:0;top:441px;width:229px;height:95px;background:linear-gradient(180deg,#9fc0d8,#3e7a4a 45%,#8d6a4e)"></div>
    <div class="caption" style="left:4px;top:526px;color:#fff">Masters Championships, 2017</div>
    <div class="elite abs" style="left:238px;top:452px">
      <h4>Our Elite Athlete Experience</h4>
      <ul><li>National Sport Performance Academy</li><li>Coastal Rugby Squad</li><li>Harbour City Summer Games</li><li>Westside Triathlon Series</li><li>Southern Nations Games</li><li>Riverside Tennis Cup</li></ul>
    </div>
  </section>

</main>
</body>
</html>
```